Ongoing Practitioner Learning Sessions
Brochure Template
Ongoing Practitioner Learning Sessions - Law
Creative Brief
Law
Professional - Lawyers. OPLS provides legal training and education seminar for lawyers.
OPLS organises and presents regular legal professional seminars throughout Australia. Our marketing is heavily based on direct mail. When we schedule our seminars we design and print brochures and send them to all lawyers that are close to the location of the seminars. The brochures contain information that relates to the specific seminars that are scheduled. Therefore, the content is tailored specifically to the events that each brochure advertises. We currently use a brochure template that accommodates four individual seminars. We have used this template for the past couple of years and would like to update/improve the design. I will upload several PDF examples of the template we currently use, but do not feel constrained by this. We are looking for some imagination and new ideas. However, it will still need to have the following elements: 1. The brochure size needs to be as follows (note – this is the equivalent of a normal DL sized brochure but double size – instead of 3 panels, each side has 6) • Width – 599 mm • Height – 214 mm • Pages – two (front and back) • Panels – 12 (6 front and 6 back) 2. The front panel needs to have the following: • Our logo • The titles of each of the four events • The location and date of the seminars (Month/Year is sufficient) 3. The design of the balance of the brochure does not need to have any other specific requirements. However, it must contain the content to advertise each event as well as a registration form and the additional information that is contained in our existing brochures. I would not be too concerned with the actual content. The design for the front panel is the most important element. Also, we need a complementary graphical design/layout for the rest of the brochure. This includes a consistent layout, fonts and other graphical elements. One thing to keep in mind is that the layout should be simple. Complex or busy designs that have a lot of photos/graphics will not work. Also, I would probably prefer graphics or abstract designs to photos. The template will need to be supplied in a format that will allow the content to be edited using InDesign. Please note that we often schedule 8, 12 or 16 seminars at the same time. As each brochure advertises 4 seminars, we often will send out 2-4 different brochures in the same envelope. If all the brochures are exactly the same design, a casual receiver may assume that all the brochures are the same and only read one of the brochures and discard the others. Therefore, we need to be able to change the graphic or design on the front cover so that two or more brochures will instantly be recognised as different. We have always done this in the past by simply having a graphic on the front that we can change the colour. For example, we can have a blue version, a red version, a green version, etc. Last thing to note is that I also wish to redesign the icon set we use to designate the compulsory subject areas for our seminars. I will create a separate project for this, but you may wish to consider submitting a design for this as well. Please see this project for the specific details, but in short, we would like to redesign the icons that we use for the compulsory subjects. At the moment we use stock art, but we would like to use a custom designed icon set.

```html
<!DOCTYPE html>
<html lang="en">
<head>
<meta charset="utf-8">
<title>Seminar Brochure Spread</title>
<link href="https://fonts.googleapis.com/css2?family=Noto+Serif:wght@700&family=Open+Sans:wght@400;600;700&display=swap" rel="stylesheet">
<style>
:root{
  --orange:#e8891c;
  --navy:#26386a;
  --grey-box:#eeeeee;
  --grey-line:#d3d3d3;
  --text:#333;
  --muted:#777;
}
*{box-sizing:border-box;margin:0;padding:0}
html,body{width:1200px;height:871px;overflow:hidden;background:#fff}
body{font-family:"Open Sans",Arial,sans-serif;color:var(--text);font-size:6px;line-height:1.45;position:relative}
.sheet{position:absolute;left:0;width:1200px;background:#fff;border:1px solid #e2e2e2}
.sheet--outer{top:0;height:428px}
.sheet--inner{top:438px;height:433px}
.panel{position:absolute;top:0;height:100%;padding:12px;overflow:hidden}
.panel+.panel{border-left:1px dashed var(--grey-line)}
.title-box{background:var(--grey-box);border-top:3px solid var(--orange);padding:9px 10px;text-align:center}
.title{font-family:"Noto Serif",Georgia,serif;color:var(--navy);font-size:13.5px;line-height:1.2;font-weight:700}
.timing{background:var(--orange);color:#fff;font-weight:600;font-size:6.5px;padding:3px 8px;margin:6px 0 7px;display:flex;gap:14px}
.cols{columns:2;column-gap:10px}
.cols p,.body p{margin-bottom:4px;text-align:justify}
ul.bullets{padding-left:9px;margin-bottom:4px}
.presenter{background:var(--grey-box);border-top:3px solid var(--orange);padding:8px 9px}
.presenter h3{color:var(--orange);font-size:9px;margin-bottom:5px;font-weight:700}
.presenter p{margin-bottom:4px;text-align:justify}
.competency{display:flex;align-items:center;gap:6px;border:1px solid var(--grey-line);border-radius:4px;padding:4px 6px;margin:6px 0;break-inside:avoid}
.competency .icon{width:14px;height:14px;border-radius:50%;background:var(--orange);flex:none}
.competency b{color:var(--orange)}
.sub-head{color:var(--orange);font-weight:700;font-size:8px;margin:6px 0 4px}
.subject{display:flex;align-items:center;gap:6px;margin:3px 0;font-size:6.5px;font-weight:600;color:var(--navy)}
.subject i{width:12px;height:12px;border-radius:50%;flex:none;display:block}
.dot-blue{background:#2f6db5}.dot-green{background:#5a9e3a}.dot-red{background:#c9402e}.dot-purple{background:#7a4f9e}
.cover{padding:0}
.brand{display:flex;align-items:center;gap:8px;padding:14px 16px 10px}
.brand .mark{width:22px;height:22px;background:var(--orange);flex:none}
.brand span{font-weight:700;color:var(--navy);font-size:10px;line-height:1.2}
.event-list{padding:4px 16px}
.event{display:flex;align-items:center;gap:8px;border-bottom:1px solid var(--grey-line);padding:7px 0}
.event i{width:16px;height:16px;background:var(--orange);border-radius:3px;flex:none;display:block}
.event span{font-size:8px;font-weight:600;color:var(--navy);line-height:1.25}
.cover-band{background:var(--orange);color:#fff;font-weight:700;font-size:11px;padding:8px 16px;margin-top:14px;display:flex;justify-content:space-between}
.cover-city{position:absolute;left:0;right:0;bottom:0;height:130px;background:linear-gradient(180deg,#8fb6dc 0%,#3f6f9f 100%)}
.cover-city .loc{position:absolute;right:14px;top:8px;text-align:right;color:#fff}
.cover-city .loc b{font-family:"Noto Serif",Georgia,serif;font-size:24px;display:block;line-height:1}
.cover-city .loc span{font-size:6.5px}
.reg-head{background:var(--orange);color:#fff;font-family:"Noto Serif",Georgia,serif;font-weight:700;font-size:14px;padding:6px 12px;margin-bottom:8px}
.reg-grid{display:grid;grid-template-columns:1fr 1fr;gap:14px}
.form-row{display:flex;align-items:center;gap:5px;margin:4px 0;font-size:6.5px}
.box{width:8px;height:8px;border:1px solid var(--muted);flex:none}
.line{flex:1;border-bottom:1px solid var(--grey-line);height:8px}
.field{display:flex;gap:5px;margin:5px 0;font-size:6.5px}
.reg-grid h4{color:var(--orange);font-size:7.5px;margin:6px 0 3px}
.note{font-size:7px;font-weight:700;color:var(--navy);margin-bottom:6px}
</style>
</head>
<body>

<section class="sheet sheet--outer">

  <article class="panel" style="left:0;width:300px">
    <div class="title-box"><h2 class="title">Preparing and Presenting Cases in the Family Court of Australia</h2></div>
    <div class="timing"><span>Timing:</span><span>Thursday, 17th November 2011</span><span>11:30 am – 12:30 pm</span></div>
    <div class="cols">
      <p>This seminar will consider the recent case law and procedural changes affecting practitioners who appear before the Family Court of Australia.</p>
      <p>An experienced barrister will guide attendees through the practical preparation of matters, from the initiating application to final hearing, with a focus on evidence and the effective presentation of a client's case.</p>
      <p>Topics to be covered include:</p>
      <ul class="bullets"><li>Procedure</li><li>Evidence</li><li>Affidavit material</li><li>Expert reports</li><li>Final hearing preparation</li></ul>
      <p>The session will also provide guidance on the court's expectations of practitioners and the rules governing conduct in court.</p>
      <p>Attendees will gain practical tips for managing complex files, working with counsel, preparing witnesses and handling disclosure.</p>
      <div class="competency"><div class="icon"></div><div><b>Competency:</b> MCLE 1 unit<br>Professional Skills</div></div>
    </div>
    <div class="presenter" style="margin-top:8px">
      <h3>About the Presenter</h3>
      <p>The presenter is a barrister practising exclusively in family law. She has appeared in numerous matters before the Family Court and the Federal Magistrates Court and regularly lectures on practice and procedure to practitioners across the state. She also sits on several professional committees.</p>
    </div>
  </article>

  <article class="panel" style="left:300px;width:300px">
    <div class="title-box" style="text-align:left"><h2 class="title">Building Law – Critical Issues</h2></div>
    <div class="timing"><span>Timing:</span><span>Thursday, 17th November 2011</span><span>1:30 pm – 2:30 pm</span></div>
    <div style="display:grid;grid-template-columns:1fr 100px;gap:9px">
      <div class="body">
        <p>This seminar will update practitioners on the critical issues arising from recent amendments to building law and the decisions of courts and tribunals dealing with residential and commercial construction disputes.</p>
        <p>Areas covered include statutory warranties, home building compensation, security of payment claims, adjudication and the interaction between contract and statute.</p>
        <p>The presenter will explain the practical steps to take when acting for owners, builders or subcontractors, and how to avoid common pitfalls in drafting and dispute resolution.</p>
        <p>Recent tribunal decisions will be examined with reference to defects, delay, variations and termination, together with the assessment of damages.</p>
        <p>The session concludes with a discussion of likely reform and strategies to protect clients from unnecessary cost and risk.</p>
        <div class="competency"><div class="icon"></div><div><b>Competency:</b> MCLE 1 unit<br>Substantive Law</div></div>
      </div>
      <div class="presenter">
        <h3>About the Presenter</h3>
        <p>The presenter is a partner of a specialist construction firm with many years of experience in building disputes.</p>
        <p>He advises owners, builders and insurers, appears regularly before the tribunal and has written widely on warranty claims.</p>
      </div>
    </div>
  </article>

  <article class="panel" style="left:600px;width:300px">
    <h2 class="title" style="text-align:left;margin-bottom:6px">MCLE Information</h2>
    <div class="body">
      <p>Attendance at each seminar counts towards your mandatory continuing legal education requirements. Each session provides one unit, and a certificate of attendance will be issued to each attendee on the day.</p>
      <p>Practitioners must complete units in each of the compulsory fields below within every practising year.</p>
    </div>
    <div class="sub-head">Compulsory Subject Areas</div>
    <div class="subject"><i class="dot-blue"></i>Ethics and Professional Responsibility</div>
    <div class="subject"><i class="dot-green"></i>Practice Management &amp; Business Skills</div>
    <div class="subject"><i class="dot-red"></i>Professional Skills</div>
    <div class="subject"><i class="dot-purple"></i>Substantive Law</div>
    <div class="body" style="margin-top:7px">
      <p>Units may be claimed on a one hour for one unit basis. Please retain your certificate for your own records, as you may be asked to produce it.</p>
      <p>For further information regarding your obligations, please contact your local law society or visit www.harbourlearnhub.com.au.</p>
    </div>
    <div class="presenter" style="margin-top:8px">
      <h3>Group Bookings</h3>
      <p>Firms registering three or more practitioners for the same session are entitled to a discount. Please contact us on (02) 9555 0142 to arrange a group booking.</p>
    </div>
  </article>

  <article class="panel cover" style="left:900px;width:300px">
    <div class="brand"><div class="mark"></div><span>Ongoing Practitioner<br>Learning Sessions</span></div>
    <div class="event-list">
      <div class="event"><i></i><span>Preparing and Presenting Cases in the Family Court of Australia</span></div>
      <div class="event"><i></i><span>Building Law – Critical Issues</span></div>
      <div class="event"><i></i><span>Statutory Demands – the Do's and Don'ts</span></div>
      <div class="event"><i></i><span>The New Succession Law – An Overview</span></div>
    </div>
    <div class="cover-band"><span>OPLS Seminars</span><span>November 2011</span></div>
    <div class="cover-city" role="img" aria-label="City skyline view in blue tones">
      <div class="loc"><b>Sydney</b><span>The Linden Hotel<br>77 Harbour Lane</span></div>
    </div>
  </article>
</section>

<section class="sheet sheet--inner">

  <article class="panel" style="left:0;width:300px">
    <div class="title-box"><h2 class="title">Statutory Demands – the Do's and Don'ts</h2></div>
    <div class="timing"><span>Timing:</span><span>Thursday, 17th November 2011</span><span>3:00 pm – 4:00 pm</span></div>
    <div class="cols">
      <p>The Corporations Act gives creditors a powerful tool to recover debts from companies. Statutory demands are frequently used, yet are often prepared incorrectly and set aside by the court.</p>
      <p>This seminar examines the requirements for a valid demand, the grounds on which a demand may be set aside and the consequences of non-compliance.</p>
      <ul class="bullets"><li>Form and service</li><li>Genuine disputes</li><li>Offsetting claims</li><li>Defects and substantial injustice</li></ul>
      <p>The presenter will also consider the strict time limits that apply and the practical steps to take when a client receives a demand.</p>
      <p>Recent decisions will be discussed to illustrate the approach of the courts and the costs risks for each party.</p>
      <div class="competency"><div class="icon"></div><div><b>Competency:</b> MCLE 1 unit<br>Substantive Law</div></div>
    </div>
    <div class="presenter" style="margin-top:8px">
      <h3>About the Presenter</h3>
      <p>The presenter is a senior associate in insolvency and commercial litigation, acting for creditors, directors and liquidators in winding up proceedings and related disputes, and lectures regularly on corporate recovery.</p>
    </div>
  </article>

  <article class="panel" style="left:300px;width:300px">
    <div class="title-box" style="text-align:left"><h2 class="title">The New Succession Law – An Overview</h2></div>
    <div class="timing"><span>Timing:</span><span>Thursday, 17th November 2011</span><span>4:15 pm – 5:15 pm</span></div>
    <div style="display:grid;grid-template-columns:1fr 100px;gap:9px">
      <div class="body">
        <p>Significant changes to succession law have commenced, affecting the making of wills, family provision claims and the administration of estates.</p>
        <p>This seminar provides a practical overview of the new legislation and its impact on everyday estate planning and probate work.</p>
        <ul class="bullets"><li>Formal validity of wills</li><li>Court authorised wills</li><li>Rectification</li><li>Family provision orders</li><li>Intestacy changes</li></ul>
        <p>Attendees will learn how the reforms alter existing practice and what precautions should be taken when taking instructions and drafting.</p>
        <p>The presenter will also address transitional provisions and the reading of earlier instruments under the new regime.</p>
        <div class="competency"><div class="icon"></div><div><b>Competency:</b> MCLE 1 unit<br>Substantive Law</div></div>
      </div>
      <div class="presenter">
        <h3>About the Presenter</h3>
        <p>The presenter is an accredited specialist in wills and estates with extensive experience in contested estates.</p>
        <p>She is a regular speaker at professional seminars and has contributed to several practice texts.</p>
      </div>
    </div>
  </article>

  <article class="panel" style="left:600px;width:600px">
    <div class="reg-head">Registration Form &amp; Tax Invoice</div>
    <div class="reg-grid">
      <div>
        <p class="note">Please register me for:</p>
        <div class="form-row"><span class="box"></span>Preparing and Presenting Cases in the Family Court</div>
        <div class="form-row"><span class="box"></span>Building Law – Critical Issues</div>
        <div class="form-row"><span class="box"></span>Statutory Demands – the Do's and Don'ts</div>
        <div class="form-row"><span class="box"></span>The New Succession Law – An Overview</div>
        <h4>Attendee Details</h4>
        <div class="field">Name<span class="line"></span></div>
        <div class="field">Firm<span class="line"></span></div>
        <div class="field">Address<span class="line"></span></div>
        <div class="field">Phone<span class="line"></span>Email<span class="line"></span></div>
        <h4>Payment</h4>
        <div class="form-row"><span class="box"></span>Cheque enclosed<span class="box"></span>Credit card</div>
        <div class="field">Card number<span class="line"></span></div>
        <div class="field">Expiry<span class="line"></span>Signature<span class="line"></span></div>
        <div class="body" style="margin-top:6px"><p>Fee per seminar $95 including GST. This form becomes a tax invoice upon payment.</p></div>
      </div>
      <div class="body">
        <h4>Venue</h4>
        <p>The Linden Hotel, 77 Harbour Lane, Sydney NSW 2000. Registration opens thirty minutes before the first session.</p>
        <h4>Cancellation</h4>
        <p>Cancellations received in writing seven days before the event will be refunded less an administration fee. Substitutions are welcome at any time.</p>
        <h4>How to Register</h4>
        <p>Phone: (02) 9555 0142<br>Email: desk@harbourlearnhub.com.au<br>Web: www.harbourlearnhub.com.au</p>
        <h4>Privacy</h4>
        <p>Your details are used only to manage your registration and to inform you of future sessions. You may ask to be removed from our mailing list at any time.</p>
        <h4>Enquiries</h4>
        <p>Ongoing Practitioner Learning Sessions, PO Box 214, Sydney NSW 2001. ABN 00 000 000 000.</p>
      </div>
    </div>
  </article>
</section>

</body>
</html>
```